Create the design of Sitelantern (in photoshop or similar)

*edit* What we wanna see is a sketch of a first page, and then in the end 5 page designs, but the main page will be the big tasks other pages are just basically pop-ups or form. *edit*

We need a web design for our new startup Sitelantern in turn will be providing web pages to smaller business. So the purpose of the page is to clearly showcase the message in a web 3.0 fashion, good design looks but function should always be the main focus.Further more we are looking for a long term relationship with a good designer / design company that can help us design the future web sites for our customers as well.

We need you to understand web, not just design. You need to be up to date with how web looks and works, and how to make it as simple and easy to use as possible for the customer and at the same time good looking.

Please look at the PDF for full description of the project.

Colors and layout are free to choose, but we really like the kind of layout that forkbreeze.com has so feel free to be inspired by them.

We want all of the pages design, but the main/landing page will be the big part, the rest are small pages that will use the same design frame as the main page.

PS. We just want the design in photoshop or illustrator format, the website will then be built in word press by word press experts (let us know if you/company also possess this knowledge)

Small to medium sized business, mostly owner/entrepreneur driven companies.

Business

• Helvetica for the win

• Great and simple design, a child should be able to understand the message and also enjoy reading it. Should be a funny website while still being professional, i.e. see postbadger.com for example.

```html
<!DOCTYPE html>
<html lang="en">
<head>
<meta charset="utf-8">
<title>Sitelantern – Most Convenient Web Ever</title>
<link rel="stylesheet" href="https://fonts.googleapis.com/css2?family=Bebas+Neue&family=Open+Sans:wght@400;600;700&family=Montserrat:wght@400;500&family=Questrial&display=swap">
<style>
:root{
  --navy:#34495e;
  --navy-dark:#2b3848;
  --coral:#f47475;
  --rose:#e0506b;
  --hero-top:#f8a491;
  --hero-bottom:#e0486a;
  --blue:#4a7fc0;
  --text:#555;
  --muted:#888;
  --light:#f3f3f3;
  --band:#efefef;
  --line:#dcdcdc;
  --white:#fff;
}
*{box-sizing:border-box;margin:0;padding:0}
html,body{width:1200px;height:2293px;overflow:hidden}
body{position:relative;background:var(--light);font-family:"Open Sans",Arial,sans-serif;color:var(--text)}
.abs{position:absolute}
a{color:inherit;text-decoration:none}

/* top bar */
.topbar{left:0;top:0;width:1200px;height:49px;background:#f8f8f8;border-bottom:1px solid #e4e4e4}
.lang-select{left:112px;top:11px;width:79px;height:24px;border:1px solid #d6d6d6;background:var(--white);font-size:12px;line-height:22px;padding-left:11px;color:#666}
.lang-select::after{content:"";position:absolute;right:10px;top:10px;border:4px solid transparent;border-top-color:#888}
.util-link{top:16px;font-size:12px;color:#666}
.search{left:939px;top:11px;width:152px;height:26px;border-radius:13px;background:#e9e9e9}

/* header */
.header{left:0;top:49px;width:1200px;height:148px;background:var(--light)}
.logo-mark{left:168px;top:69px;width:49px;height:49px;border-radius:50%;background:var(--rose)}
.logo-name{left:112px;top:113px;font-family:"Questrial",sans-serif;font-size:33px;color:var(--navy);letter-spacing:.5px}
.logo-tag{left:119px;top:150px;font-size:12px;font-weight:600;color:var(--navy)}
.nav-item{top:115px;font-size:14px;color:#444}
.nav-home{left:514px;top:107px;width:79px;height:34px;background:var(--navy);color:var(--white);font-weight:700;text-align:center;line-height:34px;border-radius:3px;font-size:14px}
.nav-order{left:1004px;top:104px;width:87px;height:38px;background:var(--coral);color:var(--white);text-align:center;line-height:38px;border-radius:3px;font-size:14px}

/* hero */
.hero{left:112px;top:197px;width:979px;height:456px;background:linear-gradient(180deg,var(--hero-top),var(--hero-bottom))}
.hero-title{left:171px;top:302px;font-family:"Bebas Neue",sans-serif;font-size:70px;color:var(--white);letter-spacing:1px}
.hero-point{left:171px;font-family:"Bebas Neue",sans-serif;font-size:24px;color:var(--white);letter-spacing:.5px;line-height:32px}
.hero-bullet{left:170px;width:22px;height:22px;border-radius:50%;background:var(--navy)}
.learn-more{left:208px;top:501px;width:107px;height:37px;background:var(--white);border-radius:3px;color:var(--navy);font-weight:700;font-size:13px;text-align:center;line-height:37px}
.hero-art{left:680px;top:252px;width:346px;height:346px;border-radius:50%;background:radial-gradient(circle at 55% 45%,#e8643d 0 22%,var(--navy) 23%)}
.slide-arrow{top:396px;width:58px;height:58px;border-radius:50%;background:var(--white);box-shadow:0 1px 4px rgba(0,0,0,.15);font-size:30px;color:#444;text-align:center;line-height:56px;font-weight:700}

/* features */
.feature{top:732px;width:320px;text-align:center}
.feature-icon{margin:0 auto;width:108px;height:108px;border-radius:50%;background:linear-gradient(135deg,#e8637a,var(--rose));display:flex;align-items:center;justify-content:center}
.feature-title{margin-top:24px;font-size:19px;color:var(--navy);line-height:24px}
.feature-text{margin-top:8px;font-size:13.5px;color:#8a8a8a;line-height:20px}
.feature-link{margin-top:4px;font-size:13.5px;color:var(--rose);text-decoration:underline;display:inline-block}

/* pricing band */
.pricing-band{left:110px;top:1065px;width:981px;height:117px;background:var(--navy)}
.pricing-text{left:138px;top:1101px;font-family:"Montserrat",sans-serif;font-size:33px;color:var(--white);letter-spacing:2px}
.btn-coral{background:var(--coral);color:var(--white);font-family:"Montserrat",sans-serif;text-align:center;border-radius:2px}
.pricing-btn{left:783px;top:1095px;width:287px;height:56px;font-size:23px;line-height:56px}

/* guarantee */
.guarantee{left:0;top:1182px;width:1200px;height:321px;background:var(--band);border-top:1px solid var(--line);border-bottom:1px solid var(--line)}
.guarantee-title{left:115px;top:1248px;font-family:"Bebas Neue",sans-serif;font-size:46px;color:var(--navy);letter-spacing:2px}
.guarantee-text{left:115px;top:1306px;font-size:20px;line-height:34px;color:#555}
.partner-dot{left:110px;top:1389px;width:66px;height:66px;border-radius:50%;background:#5bb746}
.partner-name{left:186px;top:1396px;font-family:"Open Sans",sans-serif;font-weight:700;font-size:40px;color:#222}
.mood-art{left:812px;top:1212px;width:260px;height:260px;border-radius:50%;background:#d9d9d9}

/* calculator */
.calc-title{left:0;width:1200px;text-align:center;font-family:"Bebas Neue",sans-serif;color:var(--navy);letter-spacing:2px}
.calc-field{top:1686px;height:51px;background:var(--white);border:1px solid #dedede;border-radius:2px;font-size:12.5px;color:#555;line-height:49px;padding-left:20px}
.calc-currency::after{content:"";position:absolute;right:12px;top:21px;border:5px solid transparent;border-top-color:#444}
.calc-btn{left:471px;top:1773px;width:260px;height:58px;font-size:24px;line-height:58px}

/* demo row */
.demo-text{top:1948px;font-size:21px;color:#333}
.demo-divider{top:1931px;width:1px;height:64px;background:var(--line)}
.demo-btn{left:452px;top:1937px;width:293px;height:51px;border-radius:26px;background:linear-gradient(180deg,#5a90cf,#3f73b4);color:var(--white);font-family:"Montserrat",sans-serif;font-size:19px;letter-spacing:1.5px;text-align:center;line-height:51px}

/* footer */
.footer{left:0;top:2049px;width:1200px;height:244px;background:var(--navy-dark)}
.footer-head{top:2084px;font-size:17px;color:var(--white);font-weight:600}
.contact-row{left:119px;font-size:11.5px;color:var(--white);line-height:16px}
.contact-row span{position:absolute;white-space:nowrap}
.footer-divider{top:2073px;width:1px;height:202px;background:#4a5566}
.social{top:2122px;width:30px;height:30px;border-radius:50%;background:#f2f2f2}
.subscribe-label{left:473px;top:2178px;font-size:12px;color:var(--white)}
.subscribe-input{left:474px;top:2207px;width:177px;height:33px;background:#e9e9e9;font-size:11px;color:#555;line-height:33px;padding-left:9px}
.subscribe-go{left:651px;top:2207px;width:35px;height:33px;line-height:33px;font-size:14px}
.footer-mark{left:879px;top:2072px;width:48px;height:48px;border-radius:50%;background:#f2f2f2}
.footer-name{left:0;width:1806px;text-align:center;top:2117px;font-family:"Questrial",sans-serif;font-size:32px;color:var(--white)}
.footer-tag{left:0;width:1806px;text-align:center;top:2156px;font-size:11px;color:var(--white)}
.footer-copy{left:0;width:1806px;text-align:center;top:2184px;font-size:11px;color:var(--white)}
.contact-tab{left:830px;top:2261px;width:251px;height:32px;background:#5c5f63;border:2px solid #8a8d90;border-bottom:0;color:var(--white);font-size:15px;font-weight:600;line-height:30px;padding-left:10px}
.contact-tab::after{content:"";position:absolute;right:14px;top:10px;width:8px;height:8px;border-left:2px solid #fff;border-top:2px solid #fff;transform:rotate(45deg)}
</style>
</head>
<body>

<!-- top utility bar -->
<div class="abs topbar"></div>
<div class="abs lang-select">English</div>
<a class="abs util-link" style="left:690px">My Acccount</a>
<a class="abs util-link" style="left:787px">Sign In</a>
<a class="abs util-link" style="left:849px">Need Help?</a>
<div class="abs search">
  <svg class="abs" style="left:14px;top:7px" width="12" height="12" viewBox="0 0 12 12"><circle cx="5" cy="5" r="3.6" fill="none" stroke="#999" stroke-width="1.6"/><line x1="7.6" y1="7.6" x2="11" y2="11" stroke="#999" stroke-width="1.8"/></svg>
</div>

<!-- header -->
<div class="abs header"></div>
<div class="abs logo-mark"></div>
<div class="abs logo-name">Sitelantern</div>
<div class="abs logo-tag">Most Convenient Web Ever</div>
<a class="abs nav-home">Home</a>
<a class="abs nav-item" style="left:621px">How it works</a>
<a class="abs nav-item" style="left:752px">About</a>
<a class="abs nav-item" style="left:841px">Contact</a>
<a class="abs nav-item" style="left:939px">Faq</a>
<a class="abs nav-order">Order Now</a>

<!-- hero slider -->
<div class="abs hero"></div>
<h1 class="abs hero-title">What is Sitelantern?</h1>
<div class="abs hero-bullet" style="top:387px"></div>
<p class="abs hero-point" style="left:203px;top:381px">Your website on subscription autopilot with free<br>unlimited support and updates.</p>
<div class="abs hero-bullet" style="top:451px"></div>
<p class="abs hero-point" style="left:203px;top:445px">Delivered by professionals.</p>
<a class="abs learn-more">LEARN MORE</a>
<div class="abs hero-art" role="img" aria-label="Illustration of a rocket launching through clouds in a night-sky circle"></div>
<div class="abs slide-arrow" style="left:81px">&#8249;</div>
<div class="abs slide-arrow" style="left:1062px">&#8250;</div>

<!-- features -->
<div class="abs feature" style="left:83px">
  <div class="feature-icon">
    <svg width="56" height="44" viewBox="0 0 56 44"><rect x="4" y="8" width="44" height="28" rx="2" fill="#fff" transform="rotate(-18 26 22)"/><circle cx="26" cy="22" r="8" fill="#e0506b"/><text x="26" y="27" font-family="Open Sans,sans-serif" font-weight="700" font-size="13" fill="#fff" text-anchor="middle">$</text></svg>
  </div>
  <div class="feature-title">What does it cost?</div>
  <div class="feature-text">Lorem ipsum dolor sit amet, consectetur<br>adipisicing elit, sed do eiusmod tempor<br>incidunt magna aliqua..</div>
  <a class="feature-link">Read More</a>
</div>
<div class="abs feature" style="left:441px">
  <div class="feature-icon">
    <svg width="54" height="46" viewBox="0 0 54 46"><rect x="6" y="4" width="30" height="38" rx="4" fill="#fff"/><path d="M36 12h6a6 6 0 0 1 0 12h-6" fill="none" stroke="#fff" stroke-width="5"/></svg>
  </div>
  <div class="feature-title">About The Same As 1</div>
  <div class="feature-text">Lorem ipsum dolor sit amet, consectetur<br>adipisicing elit, sed do eiusmod tempor<br>incidunt magna aliqua..</div>
  <a class="feature-link">Read More</a>
</div>
<div class="abs feature" style="left:783px">
  <div class="feature-icon">
    <svg width="54" height="56" viewBox="0 0 54 56"><rect x="8" y="14" width="28" height="38" rx="3" fill="#fff"/><path d="M8 16a8 8 0 0 1 8-10h12a8 8 0 0 1 8 10z" fill="#fff"/><path d="M36 22h6a5 5 0 0 1 5 5v10a5 5 0 0 1-5 5h-6" fill="none" stroke="#fff" stroke-width="5"/><rect x="15" y="24" width="4" height="20" fill="#e0506b"/><rect x="25" y="24" width="4" height="20" fill="#e0506b"/></svg>
  </div>
  <div class="feature-title">A day Guranteed Less Than A Relly<br>Good Night Out With THe Gang</div>
  <div class="feature-text">Lorem ipsum dolor sit amet, consectetur<br>adipisicing elit, sed do eiusmod tempor<br>incidunt magna aliqua..</div>
  <a class="feature-link">Read More</a>
</div>

<!-- pricing call to action -->
<div class="abs pricing-band"></div>
<div class="abs pricing-text">See complete pricing details here</div>
<a class="abs btn-coral pricing-btn">Request an Order Now</a>

<!-- guarantee -->
<div class="abs guarantee"></div>
<h2 class="abs guarantee-title">If you are unhappy?</h2>
<p class="abs guarantee-text">Cancel the same day, we will refund you all your<br>money and buy you a year of Tunewave subscription</p>
<div class="abs partner-dot"></div>
<div class="abs partner-name">Tunewave</div>
<div class="abs mood-art" role="img" aria-label="Sad-mood illustration in grey"></div>

<!-- conversion calculator -->
<h2 class="abs calc-title" style="top:1548px;font-size:50px">Test your website now!</h2>
<h2 class="abs calc-title" style="top:1604px;font-size:47px">How many more customers could you get every month?</h2>
<div class="abs calc-field" style="left:151px;width:184px">Visitors per month</div>
<div class="abs calc-field" style="left:345px;width:202px">Current conversion rate in %</div>
<div class="abs calc-field" style="left:558px;width:212px">Improve conversion rate, 13%</div>
<div class="abs calc-field" style="left:781px;width:181px">Average purchase in SEK</div>
<div class="abs calc-field calc-currency" style="left:972px;width:77px;padding-left:18px">EUR</div>
<a class="abs btn-coral calc-btn">Calculate Now</a>

<!-- demo row -->
<div class="abs demo-text" style="left:141px">See Pricing Details Of</div>
<div class="abs demo-divider" style="left:404px"></div>
<a class="abs demo-btn">REQUEST A DEMO</a>
<div class="abs demo-divider" style="left:795px"></div>
<div class="abs demo-text" style="left:818px">most convenient web ever</div>

<!-- footer -->
<footer class="abs footer"></footer>
<div class="abs footer-head" style="left:119px">CONTACT US</div>
<div class="abs contact-row" style="top:2117px"><span style="left:0">Phone</span><span style="left:54px">:+00 (05) 412 7730</span></div>
<div class="abs contact-row" style="top:2139px"><span style="left:0">Email</span><span style="left:54px">:xyz@sitelantern.com</span></div>
<div class="abs contact-row" style="top:2161px"><span style="left:0">Address</span><span style="left:54px">:</span><span style="left:74px">Street B 408, Elm Rise<br>51920 Harlow Rd<br>Brookfield, ST (Norland)</span></div>
<div class="abs footer-divider" style="left:433px"></div>
<div class="abs footer-head" style="left:473px">GET IN TOUCH</div>
<div class="abs social" style="left:474px"></div>
<div class="abs social" style="left:517px"></div>
<div class="abs social" style="left:560px"></div>
<svg class="abs" style="left:603px;top:2128px" width="22" height="16" viewBox="0 0 22 16"><rect x="0.5" y="0.5" width="21" height="15" rx="2" fill="#f2f2f2"/><path d="M1 1l10 8 10-8" fill="none" stroke="#2b3848" stroke-width="1.8"/></svg>
<div class="abs subscribe-label">Subscribe monthly Newsletter</div>
<div class="abs subscribe-input">Enter your email address</div>
<a class="abs btn-coral subscribe-go">GO</a>
<div class="abs footer-divider" style="left:734px"></div>
<div class="abs footer-mark"></div>
<div class="abs footer-name">Sitelantern</div>
<div class="abs footer-tag">Most Convenient Web Ever</div>
<div class="abs footer-copy">Copyright © 2014 . All rights Reserved</div>
<div class="abs contact-tab">Contact us!</div>

</body>
</html>
```